Beautiful app design for Vantor Apps

Vantor Apps makes apps for small businesses, primarily restaurants. We need a beautiful new design to update our apps with. The app design should be flexible so that it can be used as a template for several different restaurants. Interchangeable background images, fonts, and themes would be nice so that these can be applied to different restaurant types.

Target Market(s)

The target market is restaurant owners who will use the app to promote their restaurants.

Industry/Entity Type

Restaurant

Requirements
Must have
• Screens: Splash, main menu, top food menu, inner food menu or section, food menu item detail, specials page, beer menu, inner beer menu or section, beer detail page, social media menu, and About Us section. Please see screenshot images from current app for examples.
Nice to have
• Interchangeable themes, colors, fonts, and background images if applicable.

```html
<!DOCTYPE html>
<html lang="en">
<head>
<meta charset="utf-8">
<title>Menu</title>
<link rel="stylesheet" href="https://fonts.googleapis.com/css2?family=Lobster&family=Signika:wght@700&display=swap">
<style>
  :root{
    --red:#b8121a;
    --red-dark:#8e0c12;
    --red-bright:#d3262c;
    --gold:#f6b12c;
    --gold-light:#f9c552;
    --cream:#fdfcef;
    --cream-shade:#f0eedc;
    --ink:#56564a;
    --chevron:#d9d7c6;
    --white:#ffffff;
    --black:#111111;
  }
  *{box-sizing:border-box;margin:0;padding:0}
  html,body{width:676px;height:1200px;overflow:hidden;background:var(--gold)}
  .screen{
    position:absolute;left:0;top:0;width:640px;height:1136px;
    transform:scale(1.05625);transform-origin:0 0;overflow:hidden;
    background:linear-gradient(180deg,var(--gold-light),var(--gold) 60%);
    font-family:"Signika",sans-serif;font-weight:700;
  }
  .status-bar{
    position:absolute;left:0;top:0;width:640px;height:40px;background:var(--white);
    font:600 26px/40px "Helvetica Neue",Arial,sans-serif;color:var(--black);
  }
  .status-bar .time{position:absolute;left:0;width:640px;text-align:center}
  .status-bar .signal{position:absolute;left:10px;top:0}
  .status-bar .battery{position:absolute;right:12px;top:0;display:flex;align-items:center;gap:8px}
  .app-header{
    position:absolute;left:0;top:40px;width:640px;height:88px;
    background:linear-gradient(var(--red-bright),var(--red));
    box-shadow:0 4px 6px rgba(0,0,0,.25);
  }
  .app-header::after{
    content:"";position:absolute;left:0;right:0;bottom:6px;border-top:2px dashed rgba(255,255,255,.75);
  }
  .app-title{
    position:absolute;left:0;width:640px;top:10px;text-align:center;
    font:400 48px/60px "Lobster",cursive;color:var(--white);
  }
  .header-btn{
    position:absolute;top:15px;height:58px;border-radius:6px;
    background:var(--red);box-shadow:inset 0 2px 4px rgba(0,0,0,.35),0 1px 0 rgba(255,255,255,.2);
    display:flex;align-items:center;justify-content:center;gap:14px;color:var(--white);
    font:400 38px/1 "Lobster",cursive;
  }
  .header-btn.collapse{left:24px;width:116px}
  .header-btn.cart{left:498px;width:118px}
  .category-list{position:absolute;left:20px;top:152px;width:604px;list-style:none}
  .category{
    position:relative;height:113px;margin-bottom:14px;background:var(--cream);
    border-left:15px solid var(--red-bright);border-radius:4px;
    box-shadow:0 4px 0 rgba(150,110,20,.25);
  }
  .category .thumb{position:absolute;left:4px;top:4px;width:102px;height:102px}
  .category .label{
    position:absolute;left:135px;top:0;line-height:113px;
    font-family:"Signika",sans-serif;font-weight:700;font-size:37px;color:var(--ink);
    -webkit-text-stroke:0.8px var(--ink);
  }
  .category .go{
    position:absolute;right:0;top:0;width:84px;height:113px;background:var(--cream-shade);
    border-left:3px solid #e4e2cf;display:flex;align-items:center;justify-content:center;
  }
  .tab-bar{
    position:absolute;left:0;top:1020px;width:640px;height:116px;
    background:rgba(249,197,82,.88);border-top:2px solid rgba(255,255,255,.5);
  }
  .tab{position:absolute;top:10px;text-align:center;font:400 40px/1 "Lobster",cursive;color:var(--red)}
  .tab svg{display:block;margin:0 auto 4px}
  .tab.menu{left:44px;width:120px}
  .tab.account{left:456px;width:160px}
  .order-button{
    position:absolute;left:205px;top:1007px;width:230px;height:230px;border-radius:50%;
    background:radial-gradient(circle at 50% 35%,var(--red-bright),var(--red) 70%);
    border:3px solid var(--red-dark);box-shadow:0 -2px 6px rgba(0,0,0,.3);
  }
  .order-button::before{
    content:"";position:absolute;inset:10px;border-radius:50%;border:2px dashed rgba(255,255,255,.8);
  }
  .order-button .order-label{
    position:absolute;left:0;width:224px;top:72px;text-align:center;
    font:400 44px/1 "Lobster",cursive;color:var(--white);
  }
  .order-button svg{position:absolute;left:92px;top:30px}
</style>
</head>
<body>
<main class="screen">
  <div class="status-bar">
    <span class="signal">●●●○○</span>
    <span class="time">4:21 PM</span>
    <span class="battery">22%
      <svg width="46" height="22" viewBox="0 0 46 22"><rect x="1" y="1" width="40" height="20" rx="4" fill="none" stroke="#111" stroke-width="2"/><rect x="4" y="4" width="9" height="14" fill="#111"/><rect x="42" y="7" width="3" height="8" fill="#111"/></svg>
    </span>
  </div>

  <header class="app-header">
    <div class="header-btn collapse">
      <svg width="34" height="20" viewBox="0 0 34 20"><path d="M3 3 L17 16 L31 3" fill="none" stroke="#fff" stroke-width="5" stroke-linecap="round" stroke-linejoin="round"/></svg>
    </div>
    <h1 class="app-title">Menu</h1>
    <div class="header-btn cart">
      <svg width="40" height="32" viewBox="0 0 40 32"><path d="M12 12 L20 2 L28 12" fill="none" stroke="#fff" stroke-width="3"/><rect x="1" y="11" width="38" height="5" fill="#fff"/><path d="M4 16 H36 L33 31 H7 Z" fill="#fff"/><path d="M13 19 V28 M20 19 V28 M27 19 V28" stroke="#b8121a" stroke-width="3"/></svg>
      <span>2</span>
    </div>
  </header>

  <ul class="category-list">
    <li class="category"><div class="thumb" role="img" aria-label="Photo of a green salad" style="background:linear-gradient(135deg,#5f8d3a,#d8e3c0 55%,#b3312a)"></div><span class="label">Salads</span><span class="go"><svg width="26" height="42" viewBox="0 0 26 42"><path d="M4 4 L21 21 L4 38" fill="none" stroke="var(--chevron)" stroke-width="6" stroke-linecap="round"/></svg></span></li>
    <li class="category"><div class="thumb" role="img" aria-label="Photo of tomato appetizer bites" style="background:linear-gradient(160deg,#c5312a,#f2e6dc 55%,#2a2624)"></div><span class="label">Appetizers</span><span class="go"><svg width="26" height="42" viewBox="0 0 26 42"><path d="M4 4 L21 21 L4 38" fill="none" stroke="var(--chevron)" stroke-width="6" stroke-linecap="round"/></svg></span></li>
    <li class="category"><div class="thumb" role="img" aria-label="Photo of a plated entrée" style="background:radial-gradient(circle at 50% 50%,#b85a2a,#e8a23a 30%,#f4f2ee 60%)"></div><span class="label">Entrées</span><span class="go"><svg width="26" height="42" viewBox="0 0 26 42"><path d="M4 4 L21 21 L4 38" fill="none" stroke="var(--chevron)" stroke-width="6" stroke-linecap="round"/></svg></span></li>
    <li class="category"><div class="thumb" role="img" aria-label="Photo of a toasted sandwich" style="background:linear-gradient(170deg,#8ec067,#d9a45a 40%,#b3362c 60%,#eef0e6)"></div><span class="label">Sandwiches</span><span class="go"><svg width="26" height="42" viewBox="0 0 26 42"><path d="M4 4 L21 21 L4 38" fill="none" stroke="var(--chevron)" stroke-width="6" stroke-linecap="round"/></svg></span></li>
    <li class="category"><div class="thumb" role="img" aria-label="Photo of a bowl of soup" style="background:radial-gradient(circle at 55% 40%,#e2cf72,#eee6b6 40%,#dfe3e6 70%)"></div><span class="label">Soups</span><span class="go"><svg width="26" height="42" viewBox="0 0 26 42"><path d="M4 4 L21 21 L4 38" fill="none" stroke="var(--chevron)" stroke-width="6" stroke-linecap="round"/></svg></span></li>
    <li class="category"><div class="thumb" role="img" aria-label="Photo of iced drinks" style="background:linear-gradient(120deg,#4d9fb8,#b2192e 45%,#7a1020 75%,#6fb2c4)"></div><span class="label">Beverages</span><span class="go"><svg width="26" height="42" viewBox="0 0 26 42"><path d="M4 4 L21 21 L4 38" fill="none" stroke="var(--chevron)" stroke-width="6" stroke-linecap="round"/></svg></span></li>
    <li class="category"><div class="thumb" role="img" aria-label="Photo of a layered dessert" style="background:linear-gradient(160deg,#f5e8c0,#d52a2a 45%,#f2ecea 75%)"></div><span class="label">Desserts</span><span class="go"><svg width="26" height="42" viewBox="0 0 26 42"><path d="M4 4 L21 21 L4 38" fill="none" stroke="var(--chevron)" stroke-width="6" stroke-linecap="round"/></svg></span></li>
    <li class="category"><div class="thumb" role="img" aria-label="Photo of drinks" style="background:linear-gradient(160deg,#e4c26a,#c98a2a)"></div><span class="label">Drinks</span><span class="go"></span></li>
  </ul>

  <nav class="tab-bar">
    <div class="tab menu">
      <svg width="70" height="52" viewBox="0 0 70 52"><path d="M35 8 C25 2 12 2 3 5 V46 C12 43 25 43 35 49 C45 43 58 43 67 46 V5 C58 2 45 2 35 8 Z" fill="none" stroke="#b8121a" stroke-width="4" stroke-linejoin="round"/><path d="M35 8 V49" stroke="#b8121a" stroke-width="4"/><path d="M9 15 H29 M9 23 H29 M9 31 H29 M41 15 H61 M41 23 H61 M41 31 H61" stroke="#b8121a" stroke-width="3"/></svg>
      Menu
    </div>
    <div class="tab account">
      <svg width="76" height="52" viewBox="0 0 76 52"><circle cx="56" cy="18" r="15" fill="#b8121a"/><circle cx="60" cy="14" r="4" fill="#f9c552"/><path d="M44 27 L8 44 L12 50 L18 47 L20 51 L26 48 L24 44 L48 32 Z" fill="#b8121a"/></svg>
      Account
    </div>
  </nav>
  <div class="order-button">
    <svg width="40" height="32" viewBox="0 0 40 32"><path d="M12 12 L20 2 L28 12" fill="none" stroke="#fff" stroke-width="3"/><rect x="1" y="11" width="38" height="5" fill="#fff"/><path d="M4 16 H36 L33 31 H7 Z" fill="#fff"/><path d="M13 19 V28 M20 19 V28 M27 19 V28" stroke="#b8121a" stroke-width="3"/></svg>
    <span class="order-label">Order</span>
  </div>
</main>
</body>
</html>
```